Help Design the Packaging for our Nicotine Replacement Therapy

Packaging Design Brief for Brevora
We are using this contest to find a designer who can design the packaging for the full line of products listed below for our new brand. This contest will require you to provide designs for the Traditional mint in both the 2mg and 4mg, and the Traditional Cinnamon 2 mg and 4mg, plus the mint in the Modern, 2mg and 4mg. We would like to see how you propose to tie the designs together so their is clear differentiate between the products and flavors, yet it maintains brand cohesiveness.
We would like to then work with the contest winner on a 1-1 project to develop the packaging for the remaining products.
Project Overview:
Brevora is launching a new line of nicotine replacement therapy (NRT) products, including gum and lozenges in multiple flavors and strengths. The packaging design needs to reflect Brevora’s brand values of trust, warmth, professionalism, and customer-centricity while being visually appealing, functional, and easily distinguishable.
Here is our full product line up so you can design product packaging that has the potential to expand as we add more flavors.
Product Line-Up:
1. Nicotine Gum ("Traditional" because it tastes and feels like hollbeck's gum):
- Flavors: Mint, Fruit, Cinnamon
- Strengths: 2mg, 4mg
- Pack Size: 240 pieces per pack
2. Nicotine Gum (Stiffer, Playdough-Like Texture will be called "Classic"):
- Strengths: 2mg, 4mg
3. Nicotine Lozenges:
- Flavors: Mint, Citrus, Berry
- Strengths: 2mg, 4mg
- Pack Size: 120 pieces per pack
Design Objectives:
1. Brand Consistency:
- The Brevora logo should be easily recognizable across all packaging.
- The design should reflect the brand’s personality: trustworthy, professional, warm, and approachable.
- Packaging should evoke a sense of reliability and comfort, appealing to a mature audience.
2. Differentiation:
- Flavor Differentiation:
- Use distinct colors for each flavor to ensure they are easily distinguishable.
- Incorporate icons or images that represent the flavor (e.g., mint leaves for Mint, cinnamon sticks for Cinnamon).
- Strength Differentiation:
- Clearly display the nicotine strength (2mg or 4mg) in a way that stands out at a glance.
- Gum Texture Differentiation:
- Create a visual distinction between the traditional chewing gum and the stiffer, playdough-like gum while maintaining a cohesive brand look.
- Consider using different background textures, patterns, or additional design elements to indicate the different textures while ensuring they still feel part of the same family.
3. Product Type Differentiation:
- Gum vs. Lozenges:
- The lozenges should be visually distinct from the gum products while still fitting within the overall Brevora brand aesthetic.
- Consider using a different shape or design element on the lozenge packaging (e.g., a lozenge icon or a unique pattern) to differentiate them from the gum.
- Maintain consistent use of colors for flavors across both gum and lozenge packaging (e.g., Mint gum and Mint lozenges should share the same color scheme) to unify the product line.
4. Scalability:
- The design should be flexible enough to accommodate additional flavors or product variations in the future.
- Ensure that any new flavor or product type can be easily integrated into the existing design template.
Content Requirements:
1. Front of Pack:
- Brevora logo
- Flavor name and representative image
- Nicotine strength (2mg or 4mg)
- Indication of gum type (Traditional or Stiffer texture)
- Pack size (e.g., "240 Pieces")
2. Here are the die lines from the manufacturer. You will see that there are certain things that must be included on the gum packaging:
https://files.tarnowbox.net/folders/8qpe27Lm_X4v81ZsKd0n-WRyTa3GbU7Hc?usp=share_link
Overall Feel:
- The packaging should communicate that Brevora is a trustworthy, professional brand with a warm, supportive approach. It should feel modern and appeal to a broad audience both male and female.
Packaging design for all SKUs listed above, with clear differentiation between flavors, strengths, and product types.
Here is the link to the brevora logo. https://files.tarnowbox.net/file/d/7-RHbwPqJmm412LcuvzxAq3QWEtn5ZK9S/view?usp=sharing We are not opposed to the color of the dots and + sign changing to signify flavor either.
Target Market(s)
individuals 18-55+ looking to quit vaping and smoking
Industry/Entity Type
nicotine replacement therapy
Other font styles liked:
- should compliment and look good with our logo and font which is Nexa bold
Requirements
Must have
- we want to look professional and trustworthy. . .and we want a design that is cohesive across the product set and can expand and stay on brand with additional flavors.
Nice to have
- We will pick a winner and then pay that winner to do the rest of the package designs for each sku and lozenges too.

```html
<!DOCTYPE html>
<html lang="en">
<head>
<meta charset="utf-8">
<title>Brevora Gum Packaging Concepts</title>
<link href="https://fonts.googleapis.com/css2?family=Montserrat:wght@400;600;700;800&display=swap" rel="stylesheet">
<style>
  :root {
    --page: #ffffff;
    --caption: #333333;
    --mauve-soft: #a98a9d;
    --mauve-deep: #8e4274;
    --sage: #a8bfaa;
    --mint-bright: #3fd68d;
    --plum-text: #7a2f63;
    --leaf-light: #9ad94f;
    --leaf-dark: #4f9a2a;
    --logo-ink: #111111;
    --flavor-green: #5fcf3a;
    --tab-edge: #e9e3e6;
  }
  html, body {
    margin: 0;
    width: 900px;
    height: 1200px;
    overflow: hidden;
    background: var(--page);
    font-family: "Montserrat", sans-serif;
  }
  .board { position: relative; width: 900px; height: 1200px; }

  .pack {
    position: absolute;
    overflow: hidden;
    box-shadow: 0 4px 8px rgba(0,0,0,0.18);
  }
  .pack--stiffer-soft {
    left: 80px; top: 80px; width: 263px; height: 325px;
    background: var(--mauve-soft);
  }
  .pack--stiffer-bold {
    left: 110px; top: 688px; width: 240px; height: 297px;
    background: var(--mauve-soft);
  }
  .pack--traditional-soft {
    left: 547px; top: 80px; width: 273px; height: 327px;
    background: repeating-radial-gradient(circle at 50% 55%,
      var(--mauve-soft) 0 30px, var(--sage) 30px 60px);
  }
  .pack--traditional-bold {
    left: 559px; top: 688px; width: 249px; height: 300px;
    background: repeating-radial-gradient(circle at 50% 55%,
      var(--mauve-deep) 0 28px, var(--sage) 28px 56px);
  }

  .stripes {
    position: absolute; left: 0; top: 0; right: 0;
  }
  .pack--stiffer-soft .stripes {
    height: 178px;
    background: repeating-linear-gradient(90deg,
      var(--sage) 0 12px, transparent 12px 24px);
    background-position: 6px 0;
  }
  .pack--stiffer-bold .stripes {
    height: 165px;
    background: repeating-linear-gradient(90deg,
      var(--mint-bright) 0 11px, transparent 11px 22px);
    background-position: 6px 0;
  }
  .base-band { position: absolute; left: 0; right: 0; bottom: 0; }
  .pack--stiffer-soft .base-band { height: 66px; background: var(--sage); }
  .pack--stiffer-bold .base-band { height: 60px; background: var(--mauve-deep); }

  .type-tab {
    position: absolute; left: 50%; top: -3px;
    transform: translateX(-50%);
    width: 96px; height: 38px;
    background: var(--mauve-soft);
    border: 3px solid var(--tab-edge);
    border-radius: 0 0 8px 8px;
    box-sizing: border-box;
    display: flex; align-items: flex-start; justify-content: center;
    padding-top: 6px;
    font-size: 10px; font-weight: 400; color: #ffffff;
  }
  .pack--stiffer-bold .type-tab { width: 88px; height: 35px; font-size: 9.5px; }

  .brand {
    position: absolute; left: 0; right: 0;
    text-align: center;
    font-weight: 800;
    color: var(--logo-ink);
    letter-spacing: -0.5px;
    line-height: 1;
  }
  .brand-dot {
    display: inline-block; width: 9px; height: 9px; border-radius: 50%;
    background: #ffffff; vertical-align: top; margin-right: 3px;
  }
  .pack--stiffer-soft .brand { top: 275px; font-size: 38px; }
  .pack--stiffer-bold .brand { top: 177px; font-size: 36px; }
  .pack--traditional-soft .brand { top: 155px; font-size: 46px; }
  .pack--traditional-bold .brand { top: 143px; font-size: 42px; }
  .pack--traditional-bold .brand-dot { background: var(--flavor-green); }

  .flavor {
    position: absolute; left: 0; right: 0;
    display: flex; align-items: center; justify-content: center; gap: 6px;
    font-weight: 700; text-transform: uppercase;
    color: var(--plum-text); text-align: center; line-height: 1.1;
  }
  .flavor::before, .flavor::after {
    content: ""; height: 1.5px; background: currentColor; width: 36px;
  }
  .pack--stiffer-soft .flavor { top: 236px; font-size: 11px; }
  .pack--stiffer-bold .flavor { top: 212px; font-size: 10.5px; }
  .pack--traditional-soft .flavor { top: 198px; font-size: 11.5px; }
  .pack--traditional-bold .flavor { top: 185px; font-size: 11.5px; color: var(--flavor-green); }
  .pack--stiffer-soft .flavor::before, .pack--stiffer-soft .flavor::after { width: 40px; }
  .pack--stiffer-bold .flavor::before, .pack--stiffer-bold .flavor::after { width: 32px; }

  .flavor-art {
    position: absolute; left: 50%; transform: translateX(-50%);
    width: 54px; height: 44px; border-radius: 50% 50% 45% 45%;
    background: radial-gradient(circle at 50% 40%, var(--leaf-light), var(--leaf-dark));
  }
  .pack--stiffer-soft .flavor-art { top: 258px; }
  .pack--stiffer-bold .flavor-art { top: 232px; width: 50px; height: 40px; }
  .pack--traditional-soft .flavor-art { top: 232px; }
  .pack--traditional-bold .flavor-art { top: 220px; width: 50px; height: 42px; }

  .count {
    position: absolute; left: 10px;
    font-weight: 800; line-height: 0.9; text-align: center;
  }
  .count small { display: block; font-size: 6px; font-weight: 700; }
  .strength { position: absolute; right: 14px; font-weight: 800; }
  .pack--stiffer-soft .count { bottom: 14px; font-size: 11px; color: var(--plum-text); }
  .pack--stiffer-soft .strength { bottom: 12px; font-size: 13px; color: var(--plum-text); }
  .pack--stiffer-bold .count { bottom: 14px; font-size: 10px; color: var(--mint-bright); }
  .pack--stiffer-bold .strength { bottom: 12px; font-size: 12px; color: var(--mint-bright); }
  .pack--traditional-soft .count { left: 13px; bottom: 20px; font-size: 12px; color: var(--plum-text); }
  .pack--traditional-soft .strength { right: 12px; bottom: 20px; font-size: 14px; color: var(--plum-text); }
  .pack--traditional-bold .count { left: 17px; bottom: 16px; font-size: 11px; color: var(--logo-ink); }
  .pack--traditional-bold .strength { right: 18px; bottom: 16px; font-size: 13px; color: var(--logo-ink); }

  .caption {
    position: absolute; width: 220px; text-align: center;
    font-size: 17px; font-weight: 700; color: var(--caption); line-height: 25px;
    margin: 0;
  }
</style>
</head>
<body>
<main class="board">

  <section class="pack pack--stiffer-soft" aria-label="Stiffer mint pack, soft palette">
    <div class="stripes"></div>
    <div class="base-band"></div>
    <div class="type-tab">nicotine gums</div>
    <div class="brand" style="top:187px"><span class="brand-dot"></span>Brevora</div>
    <div class="flavor">Stiffer Mint</div>
    <div class="flavor-art" role="img" aria-label="Mint leaf illustration"></div>
    <div class="count">240<small>MINTS</small></div>
    <div class="strength">4MG</div>
  </section>
  <p class="caption" style="left:102px; top:557px">Design 1<br>(stiffer)</p>

  <section class="pack pack--traditional-soft" aria-label="Traditional mint pack, soft palette">
    <div class="brand"><span class="brand-dot"></span>Brevora</div>
    <div class="flavor">Traditional<br>Mint</div>
    <div class="flavor-art" role="img" aria-label="Mint leaf illustration"></div>
    <div class="count">240<small>MINTS</small></div>
    <div class="strength">4MG</div>
  </section>
  <p class="caption" style="left:588px; top:557px">Design 3<br>(traditional)</p>

  <section class="pack pack--stiffer-bold" aria-label="Stiffer mint pack, bold palette">
    <div class="stripes"></div>
    <div class="base-band"></div>
    <div class="type-tab">nicotine gums</div>
    <div class="brand"><span class="brand-dot"></span>Brevora</div>
    <div class="flavor">Stiffer Mint</div>
    <div class="flavor-art" role="img" aria-label="Mint leaf illustration"></div>
    <div class="count">240<small>MINTS</small></div>
    <div class="strength">4MG</div>
  </section>
  <p class="caption" style="left:105px; top:1112px">Design 2<br>(stiffer)</p>

  <section class="pack pack--traditional-bold" aria-label="Traditional mint pack, bold palette">
    <div class="brand"><span class="brand-dot"></span>Brevora</div>
    <div class="flavor">Traditional<br>Mint</div>
    <div class="flavor-art" role="img" aria-label="Mint leaf illustration"></div>
    <div class="count">240<small>MINTS</small></div>
    <div class="strength">4MG</div>
  </section>
  <p class="caption" style="left:588px; top:1112px">Design 4<br>(traditional)</p>

</main>
</body>
</html>
```